Kestrel Capital Circle - Paradigm Shifting Investment Vehicle in Bali*

The presentation is for the Kestrel Capital Circle, a future-thinking and paradigm-shifting leadership collective that is aimed at uniting conscious investors with New Earth projects in Bali, Indonesia. We want to create a presentation pitch deck to investors that encompasses that concept, pairing our royal purple logo with elements of natural green, or white/black that feels organic, purposeful and powerful. Example of our investor deck is attached.

Target Market(s)

High Net Worth Conscious Individuals, Wealthy Nomads looking to move to Bali, community building leaders

Industry/Entity Type

Investment

Logo Text

Kestrel Capital Circle

Font styles to use
Serif
Sans Serif

Colors
6b449b
886aae
b8a6cd
acd037
cadf82
add136
00a990
33b8a4
86cfc6

Requirements
Must have
• Our name of "Kestrel Capital Circle" or "KCC"
Nice to have
• keywords: consciousness, transformational, healing, new paradigm, progress, New Earth, abundance, regenerative, royal, natural, organic, sustainability, future, dream, creation, co-creation
Should not have
• Boring, corporate look

```html
<!DOCTYPE html>
<html lang="en">
<head>
<meta charset="UTF-8">
<title>Kestrel Capital Circle – Investor Deck</title>
<link href="https://fonts.googleapis.com/css2?family=Playfair+Display:wght@600;700&family=Lato:wght@400;700;900&display=swap" rel="stylesheet">
<style>
:root{
  --page:#f6f5f7;
  --plum-deep:#2e1433;
  --plum:#4a2150;
  --plum-mid:#6b2f62;
  --royal:#6b449b;
  --lavender:#886aae;
  --lilac:#b8a6cd;
  --lime:#acd037;
  --lime-soft:#cadf82;
  --teal:#00a990;
  --teal-mid:#33b8a4;
  --teal-soft:#86cfc6;
  --sunset:#c9745f;
  --white:#ffffff;
  --ink:#222;
}
*{margin:0;padding:0;box-sizing:border-box}
html,body{width:845px;height:1200px;overflow:hidden}
body{background:var(--page);position:relative;font-family:'Lato',sans-serif;color:var(--white)}
.slide{position:absolute;width:378px;height:212px;overflow:hidden;
  background:linear-gradient(160deg,var(--plum) 0%,var(--plum-deep) 100%);box-shadow:0 2px 6px rgba(0,0,0,.18)}
.col-l{left:37px}.col-r{left:430px}
.row-1{top:62px}.row-2{top:290px}.row-3{top:518px}.row-4{top:746px}
.scene{position:absolute;left:0;right:0;bottom:0;height:90px;
  background:linear-gradient(180deg,rgba(107,47,98,0) 0%,rgba(150,70,110,.55) 55%,rgba(30,10,30,.9) 100%)}
.slide-tag{position:absolute;left:14px;top:9px;font-size:4.5px;letter-spacing:.4px;color:var(--lilac);text-transform:uppercase}
.slide-title{position:absolute;left:14px;top:19px;font-family:'Playfair Display',serif;font-weight:700;font-size:11px}
.brand-mark{position:absolute;right:10px;top:8px;width:28px;height:28px;background:var(--white);
  color:var(--royal);font-family:'Lato',sans-serif;font-weight:900;font-size:7px;display:flex;align-items:center;justify-content:center}
.body-text{position:absolute;left:14px;font-size:5px;line-height:1.5;color:#e6dcea}
.list{position:absolute;list-style:none;font-size:5px;line-height:1.9;color:#efe8f2}
.list li::before{content:"";display:inline-block;width:4px;height:4px;margin-right:4px;background:var(--lime);border-radius:50%;vertical-align:middle}
.list.teal li::before{background:var(--teal-soft)}
/* cover */
.cover{background:linear-gradient(180deg,#5a3470 0%,#7e4a78 35%,#b9756e 58%,#4c2a49 72%,#2a1530 100%)}
.cover .brand-mark{left:16px;right:auto;top:14px;width:24px;height:24px;font-size:6px}
.cover-title{position:absolute;left:16px;top:62px;font-family:'Playfair Display',serif;font-weight:700;font-size:15px}
.cover-sub{position:absolute;left:16px;top:84px;font-size:5.5px;color:#f0e6ee}
.cta{position:absolute;left:16px;top:98px;background:var(--lime);color:var(--plum-deep);font-size:5px;font-weight:700;padding:3px 14px}
/* timeline */
.steps{position:absolute;left:14px;right:14px;top:96px;display:flex;gap:3px}
.step{flex:1;font-size:4.6px;color:#e6dcea}
.step b{display:block;font-size:5px;color:var(--white);margin-bottom:3px}
.step i{display:block;height:5px;margin-bottom:4px}
/* table */
.fee-table{position:absolute;left:14px;top:60px;width:350px;border-collapse:collapse;font-size:5px}
.fee-table th{background:var(--plum-deep);color:var(--white);padding:4px;text-align:left}
.fee-table td{padding:3.5px 4px;color:var(--white)}
.fee-table tr:nth-child(odd) td{background:var(--teal)}
.fee-table tr:nth-child(even) td{background:var(--teal-mid)}
.photo{position:absolute;right:18px;top:48px;width:150px;height:120px;
  background:linear-gradient(160deg,#dfe4e6 0%,#a9b3a3 45%,#5e6b53 100%)}
.foot{position:absolute;left:0;top:1012px;width:845px;text-align:center;color:var(--ink);
  font-family:'Lato',sans-serif;font-weight:900;font-size:19px;letter-spacing:3px}
</style>
</head>
<body>

<!-- Cover -->
<section class="slide cover col-l row-1">
  <div class="brand-mark">KCC</div>
  <h1 class="cover-title">Kestrel Capital Circle</h1>
  <p class="cover-sub">Invest in New Earth Projects in Bali, Indonesia</p>
  <span class="cta">Schedule a Discovery Call</span>
</section>

<!-- Becoming a member -->
<section class="slide col-r row-1">
  <div class="slide-tag">Kestrel Capital Circle</div>
  <h2 class="slide-title">Becoming a Member</h2>
  <div class="brand-mark">KCC</div>
  <p class="body-text" style="top:44px;width:250px">Membership is by invitation for conscious investors who share our vision of regenerative growth and co-creation in Bali.</p>
  <div class="steps">
    <div class="step"><b>Step 1</b><i style="background:var(--lavender)"></i>Submit your application</div>
    <div class="step"><b>Step 2</b><i style="background:var(--lime)"></i>Meet the founders</div>
    <div class="step"><b>Step 3</b><i style="background:var(--royal)"></i>Sign the charter</div>
    <div class="step"><b>Step 4</b><i style="background:var(--teal)"></i>Join the circle</div>
  </div>
</section>

<!-- Fee table -->
<section class="slide col-l row-2">
  <div class="slide-tag">Kestrel Capital Circle</div>
  <h2 class="slide-title">Membership Fee Breakdown</h2>
  <div class="brand-mark">KCC</div>
  <p class="body-text" style="top:44px">Transparent tiers aligned with your level of participation.</p>
  <table class="fee-table">
    <tr><th>Tier</th><th>Annual Fee</th><th>Benefits</th></tr>
    <tr><td>Seed</td><td>$5,000</td><td>Community events</td></tr>
    <tr><td>Grove</td><td>$10,000</td><td>Deal previews</td></tr>
    <tr><td>Canopy</td><td>$25,000</td><td>Co-investment rights</td></tr>
    <tr><td>Forest</td><td>$50,000</td><td>Board seat access</td></tr>
  </table>
</section>

<!-- Fee chart -->
<section class="slide col-r row-2">
  <div class="scene" role="img" aria-label="Palm tree silhouettes against a purple sunset"></div>
  <div class="slide-tag">Kestrel Capital Circle</div>
  <h2 class="slide-title">Membership Fee Breakdown</h2>
  <div class="brand-mark">KCC</div>
  <p class="body-text" style="top:44px">How each membership fee supports the circle.</p>
  <ul class="list" style="left:14px;top:62px">
    <li>Project due diligence</li><li>Community gatherings</li><li>Land stewardship</li><li>Operations</li><li>Healing retreats</li>
  </ul>
  <svg style="position:absolute;left:225px;top:56px" width="100" height="100" viewBox="0 0 100 100">
    <g fill="none" stroke-width="16" transform="rotate(-90 50 50)">
      <circle cx="50" cy="50" r="38" stroke="#b8a6cd"/>
      <circle cx="50" cy="50" r="38" stroke="#886aae" stroke-dasharray="95 239"/>
      <circle cx="50" cy="50" r="38" stroke="#c0508f" stroke-dasharray="60 239" stroke-dashoffset="-95"/>
      <circle cx="50" cy="50" r="38" stroke="#6b449b" stroke-dasharray="45 239" stroke-dashoffset="-155"/>
    </g>
  </svg>
</section>

<!-- Why -->
<section class="slide col-l row-3">
  <div class="scene" role="img" aria-label="Palm tree silhouettes against a purple sunset"></div>
  <div class="slide-tag">Kestrel Capital Circle</div>
  <h2 class="slide-title">Why KCC Investments?</h2>
  <div class="brand-mark">KCC</div>
  <p class="body-text" style="top:44px;width:300px">We back regenerative ventures that heal land and community while delivering lasting returns for members.</p>
  <ul class="list" style="left:14px;top:66px">
    <li>Vetted local partners</li><li>Transparent reporting</li><li>Shared impact goals</li><li>Long-term abundance</li>
  </ul>
</section>

<!-- Opportunities -->
<section class="slide col-r row-3">
  <div class="scene" role="img" aria-label="Palm tree silhouettes against a purple sunset"></div>
  <div class="slide-tag">Kestrel Capital Circle</div>
  <h2 class="slide-title">Investment Opportunities</h2>
  <div class="brand-mark">KCC</div>
  <ul class="list" style="left:14px;top:46px">
    <li>Eco villages</li><li>Permaculture farms</li><li>Healing centres</li><li>Renewable energy</li>
  </ul>
  <ul class="list" style="left:170px;top:46px">
    <li>Wellness resorts</li><li>Regenerative tourism</li><li>Creative hubs</li><li>Clean water</li>
  </ul>
  <p class="body-text" style="top:110px;width:330px">Each opportunity is reviewed by the circle for purpose, sustainability and return before it is offered.</p>
</section>

<!-- Project -->
<section class="slide col-l row-4">
  <div class="slide-tag">Kestrel Capital Circle</div>
  <h2 class="slide-title">Sunda Reef Estate</h2>
  <div class="brand-mark">KCC</div>
  <p class="body-text" style="top:48px;width:160px">A regenerative coastal village on the north shore, blending organic farming, eco homes and a healing retreat for the new paradigm.</p>
  <div class="photo" role="img" aria-label="Open pavilion with round window overlooking green hills"></div>
</section>

<!-- Accelerate -->
<section class="slide col-r row-4">
  <div class="scene" role="img" aria-label="Palm tree silhouettes against a purple sunset"></div>
  <div class="slide-tag">Kestrel Capital Circle</div>
  <h2 class="slide-title">Accelerate and Incubate</h2>
  <div class="brand-mark">KCC</div>
  <p class="body-text" style="top:44px;width:300px">We help founders grow transformational ideas into thriving New Earth ventures.</p>
  <ul class="list teal" style="left:14px;top:62px">
    <li>Mentorship</li><li>Seed funding</li><li>Legal guidance</li><li>Market access</li>
  </ul>
  <ul class="list teal" style="left:170px;top:62px">
    <li>Team building</li><li>Impact metrics</li><li>Community network</li><li>Brand creation</li>
  </ul>
</section>

<p class="foot">THANKS FOR WATCHING</p>
</body>
</html>
```